KRV Ltd Business Card
Professional Biz Card for Kestrel Ridge Ventures IBC Ltd
KRV Ltd Business Card -
Creative Brief
Professional
Milo Harwick
President & CEO
milo@kestrelridgeventures.biz
www.kestrelridgeventures.biz
Skype ID: mharwick should be added.
www.kestrelridgeventures.biz & perhaps a large version of my logo.

```html
<!DOCTYPE html>
<html lang="en">
<head>
<meta charset="utf-8">
<title>KRV Ltd Business Card</title>
<link href="https://fonts.googleapis.com/css2?family=Michroma&family=Open+Sans:wght@400;700&display=swap" rel="stylesheet">
<style>
  :root {
    --page: #ffffff;
    --card-light-top: #f7f7f7;
    --card-light-bottom: #d9d9d9;
    --card-dark: #0b0b0b;
    --swoosh: #bdbdbd;
    --mark-on-light: #9c9c9c;
    --mark-on-dark: #c9c9c9;
    --ink-dark: #222222;
    --ink-light: #ffffff;
    --card-shadow: 0 3px 10px rgba(0,0,0,0.28);
  }
  * { margin: 0; padding: 0; box-sizing: border-box; }
  html, body { width: 1200px; height: 727px; overflow: hidden; background: var(--page); }
  .canvas { position: relative; width: 1200px; height: 727px; }
  .card {
    position: absolute;
    width: 556px; height: 330px;
    border-radius: 16px;
    overflow: hidden;
    box-shadow: var(--card-shadow);
    font-family: "Open Sans", Arial, sans-serif;
  }
  .card--light { background: linear-gradient(180deg, var(--card-light-top), var(--card-light-bottom)); }
  .card--dark { background: var(--card-dark); }
  .card--front { left: 392px; top: 8px; background: linear-gradient(180deg, var(--card-light-top), var(--card-light-bottom)); }
  .card--back-light { left: 19px; top: 384px; }
  .card--back-dark { left: 621px; top: 384px; }

  .card__sweep { position: absolute; inset: 0; width: 100%; height: 100%; }

  .wordmark {
    position: absolute;
    font-family: "Michroma", Arial, sans-serif;
    font-weight: 400;
    letter-spacing: 4px;
    white-space: nowrap;
  }
  .card--front .wordmark {
    left: 26px; top: 146px;
    font-size: 28px; letter-spacing: 2px;
    color: var(--mark-on-light);
  }
  .card--back-light .wordmark,
  .card--back-dark .wordmark { left: 0; right: 0; top: 112px; text-align: center; font-size: 62px; }
  .card--back-light .wordmark { color: var(--mark-on-light); }
  .card--back-dark .wordmark { color: var(--mark-on-dark); }

  .identity { position: absolute; right: 28px; top: 20px; text-align: right; color: var(--ink-light); }
  .identity__name { font-size: 22px; font-weight: 700; line-height: 1.2; }
  .identity__title { font-size: 13px; line-height: 1.4; }

  .contacts { position: absolute; right: 28px; top: 190px; text-align: right; color: var(--ink-light); font-size: 13.5px; line-height: 1.55; }
  .contacts dt { display: inline; font-weight: 700; }
  .contacts dd { display: inline; }
  .contacts div { white-space: nowrap; }

  .site-url { position: absolute; left: 0; right: 0; bottom: 20px; text-align: center; font-size: 13px; font-weight: 700; }
  .card--back-light .site-url { color: var(--ink-dark); }
  .card--back-dark .site-url { color: var(--ink-light); }
</style>
</head>
<body>
<main class="canvas">

  <section class="card card--front" aria-label="Card front">
    <svg class="card__sweep" viewBox="0 0 556 330" preserveAspectRatio="none" aria-hidden="true">
      <path d="M262 0 C 208 80, 200 230, 250 330 L 556 330 L 556 0 Z" fill="var(--swoosh)"/>
      <path d="M290 0 C 232 80, 226 230, 272 330 L 556 330 L 556 0 Z" fill="var(--card-dark)"/>
    </svg>
    <div class="wordmark">KRV Ltd</div>
    <div class="identity">
      <p class="identity__name">Milo Harwick</p>
      <p class="identity__title">President &amp; CEO</p>
    </div>
    <dl class="contacts">
      <div><dt>Cell :</dt> <dd>+86 139 2047 5521</dd></div>
      <div><dt>Email :</dt> <dd>milo@kestrelridgeventures.biz</dd></div>
      <div><dt>Web :</dt> <dd>www.kestrelridgeventures.biz</dd></div>
      <div><dt>Skype :</dt> <dd>mharwick</dd></div>
    </dl>
  </section>

  <section class="card card--light card--back-light" aria-label="Card back, light">
    <div class="wordmark">KRV Ltd</div>
    <p class="site-url">www.kestrelridgeventures.biz</p>
  </section>

  <section class="card card--dark card--back-dark" aria-label="Card back, dark">
    <div class="wordmark">KRV Ltd</div>
    <p class="site-url">www.kestrelridgeventures.biz</p>
  </section>

</main>
</body>
</html>
```